IV Bag Graphic for IV Therapy Bar

Hello we are offering an IV Therapy Bar to our medical practice. We already have a logo would like a cool design label for the IV bag. We will utilize this label for social media advertising, a sticker for the saline bag and marketing material. Woukd like something unique, sharp, bold and professional. We signed up for the Social Media package so the design will need to hold and be creative.

Target Market(s)

25-35 yrs old

Requirements
Must have
• Velmora Clinical Research name and logo- Clear inference it is IV therapy
Nice to have
• Innovation- Lines to write Name - Also please give examples of the different IV therapies (Myers cocktail) etc (screenshot example of therapies is attached)
Should not have
• In the attached examples the packaging and label are black, in open.

```html
<!DOCTYPE html>
<html lang="en">
<head>
<meta charset="utf-8">
<title>Myers Cocktail IV Label</title>
<link href="https://fonts.googleapis.com/css2?family=Montserrat:wght@500;600;700;800&display=swap" rel="stylesheet">
<style>
  :root {
    --canvas: #e6e6e6;
    --label: #ffffff;
    --label-tint: #f1f1f1;
    --ink-dark: #3a3a3a;
    --ink-mid: #5c5c5c;
    --ink-soft: #6f6f6f;
    --pill: #777777;
    --rule: #dcdcdc;
    --band-start: #3b3b3b;
    --band-end: #5e5e5e;
    --white: #ffffff;
  }
  * { box-sizing: border-box; margin: 0; padding: 0; }
  html, body {
    width: 1200px; height: 963px; overflow: hidden;
    background: var(--canvas);
    font-family: "Montserrat", sans-serif;
  }
  .label {
    position: absolute; left: 297px; top: 51px;
    width: 605px; height: 860px;
    background: linear-gradient(160deg, var(--label-tint) 0%, var(--label) 55%, var(--label-tint) 100%);
    box-shadow: 0 2px 6px rgba(0,0,0,0.18);
    overflow: hidden;
  }
  .brand {
    position: absolute; top: 44px; left: 0; width: 100%;
    display: flex; justify-content: center; align-items: center; gap: 16px;
  }
  .brand-mark {
    width: 62px; height: 62px; border-radius: 50%;
    background: var(--ink-soft);
  }
  .brand-name {
    color: var(--ink-mid); font-weight: 600; line-height: 1;
  }
  .brand-name .primary { display: block; font-size: 58px; letter-spacing: -1px; }
  .brand-name .secondary { display: block; font-size: 27px; margin-top: 6px; }
  .title {
    position: absolute; top: 172px; left: 0; width: 100%;
    text-align: center; color: var(--ink-dark); font-weight: 800;
    line-height: 0.92; letter-spacing: -2px;
  }
  .title .line-one { display: block; font-size: 98px; }
  .title .line-two { display: block; font-size: 96px; }
  .pill {
    position: absolute; top: 360px; left: 52px; width: 496px; height: 50px;
    border-radius: 25px; background: var(--pill);
    color: var(--white); font-weight: 700; font-size: 32px;
    display: flex; align-items: center; justify-content: center;
    letter-spacing: 0.3px;
  }
  .ingredients {
    position: absolute; top: 438px; left: 50%; transform: translateX(-50%);
    width: 264px; list-style: none; text-align: center;
  }
  .ingredients li {
    font-size: 22px; font-weight: 500; color: var(--ink-dark);
    height: 40px; line-height: 38px;
    border-bottom: 1px solid var(--rule);
  }
  .ingredients li:last-child { border-bottom: none; }
  .features {
    position: absolute; top: 712px; left: 0; width: 100%; height: 72px;
    background: linear-gradient(90deg, var(--band-start), var(--band-end) 50%, var(--band-start));
    display: flex; align-items: center; padding: 0 26px;
  }
  .feature {
    display: flex; align-items: center; gap: 8px;
    color: var(--white); font-weight: 700; font-size: 20px; line-height: 1.05;
  }
  .feature svg { width: 50px; height: 50px; flex: none; }
  .divider { width: 1px; height: 44px; background: rgba(255,255,255,0.6); margin: 0 11px; }
  .volume {
    position: absolute; top: 806px; left: 58px;
    font-size: 28px; font-weight: 800; color: var(--ink-mid); letter-spacing: 0.5px;
  }
</style>
</head>
<body>
  <div class="label">
    <div class="brand">
      <span class="brand-mark"></span>
      <span class="brand-name">
        <span class="primary">VELMORA</span>
        <span class="secondary">CLINICAL RESEARCH</span>
      </span>
    </div>

    <h1 class="title">
      <span class="line-one">MYERS</span>
      <span class="line-two">COCKTAIL</span>
    </h1>

    <div class="pill">IV THERAPY TREATMENT</div>

    <ul class="ingredients">
      <li>Calcium Chloride</li>
      <li>Magnesium Chloride</li>
      <li>Vitamin-B Complex</li>
      <li>Vitamin-B 12</li>
      <li>Vitamin C</li>
      <li>Folic Acid</li>
    </ul>

    <div class="features">
      <div class="feature">
        <svg viewBox="0 0 50 50" aria-hidden="true">
          <circle cx="25" cy="25" r="22" fill="none" stroke="#fff" stroke-width="2.5"/>
          <path d="M16 26 L22 32 L34 19" fill="none" stroke="#fff" stroke-width="3" stroke-linecap="round" stroke-linejoin="round"/>
        </svg>
        <span>Natural<br>Therapy</span>
      </div>
      <span class="divider"></span>
      <div class="feature">
        <svg viewBox="0 0 50 50" aria-hidden="true">
          <circle cx="25" cy="25" r="22" fill="none" stroke="#fff" stroke-width="2.5"/>
          <path d="M13 25 H37 A12 10 0 0 1 13 25 Z" fill="#fff"/>
        </svg>
        <span>Quality<br>Ingredients</span>
      </div>
      <span class="divider"></span>
      <div class="feature">
        <svg viewBox="0 0 50 50" aria-hidden="true">
          <circle cx="25" cy="25" r="22" fill="none" stroke="#fff" stroke-width="2.5"/>
          <circle cx="25" cy="23" r="9" fill="#fff"/>
        </svg>
        <span>Product of<br>Nuvera</span>
      </div>
    </div>

    <div class="volume">1000ML</div>
  </div>
</body>
</html>
```